Counseling Practice Business Card

I need a professional looking business card incorporating my new logo that was just completed. Card needs to incorporate my name and title, description of my specialty, my address, my phone number, my fax number, my email and my website URL. I need to be able to choose design on/with different paper colors and textures.
I do not have a lot of business card ideas so I am open to anything but I want bold,sharp, clear card without additional designs other than my logo (see attached file info). I am open to different color backgrounds or paper colors including black. I do not like traditional brackets around area codes in phone number or dashes between numbers in phone number. Am open to other ways of presenting including periods between numbers as appropriate. I do not know enough to know what I like yet but I want card to coordinate and work together with my logo. My practice emphasizes natural mental health interventions so any use of color (with background paper color or the blue and green in my logo) that elicits nature is nice. In addition to black, any natural brown or wood looking background might be desirable also. Most of the offerings so far look very similar and boring.

Target Market(s)

Potential therapy clients and other professionals

Contact Information for Business Card

Card information:
Marcus T. Whitfield, Ph.D.
Licensed Clinical Psychologist
Integrative Health Coach
4812 Ferndale Pkwy NW
Suite 730
Elmvale, OR 97530
(483) 555-0142 phone
(483) 555-0186 fax
drmarcuswhitfield@kelvora.com
pathbloomcounseling.com

Font styles to use
Serif
Sans Serif
Other font styles liked:
• anything that you think looks crisp, clear and easily readable

Requirements
Must have
• Any color used should coordinate with my logo design (see attached files).
• Card should be printed horizontally so top and bottom are longest sides of rectangle.
• Background color or paper color should complement and highlight logo. Do not like a white background. black, grey, brown or any color my logo would blend well with.
Nice to have
• I would like designer to utilize color to highlight letters/name or phone-fax-web symbols.
• Bottom edge of card could be highlighted if appropriate to an idea.
Should not have
• I would NOT want the card to have a pure white background at all.
• No clear cards.
• Cards should be oriented with long sides on bottom and top, NOT sides. DO NOT LIKE THIS THIN TALL ORIENTATION.

```html
<!DOCTYPE html>
<html lang="en">
<head>
<meta charset="utf-8">
<title>Pathbloom Counseling – Business Card</title>
<link rel="stylesheet" href="https://fonts.googleapis.com/css2?family=Roboto:wght@400;500&family=Roboto+Condensed:wght@700&display=swap">
<style>
  :root {
    --backdrop: #7a5236;
    --card: #16171a;
    --brand-blue: #2d78c2;
    --brand-green: #1a7a3e;
    --text-light: #d9d9d9;
    --rule: #8a8a8a;
  }
  * { margin: 0; padding: 0; box-sizing: border-box; }
  html, body { width: 1200px; height: 960px; overflow: hidden; }
  body {
    position: relative;
    background: var(--backdrop);
    font-family: "Roboto", Arial, sans-serif;
  }
  .card {
    position: absolute;
    background: var(--card);
    box-shadow: 0 3px 8px rgba(0,0,0,.45);
  }
  .card--front { left: 314px; top: 113px; width: 601px; height: 342px; }
  .card--back  { left: 312px; top: 472px; width: 599px; height: 343px; }

  .brand {
    position: absolute;
    display: flex;
    align-items: center;
    gap: 8px;
    color: var(--brand-blue);
    font-weight: 500;
  }
  .brand__dot {
    width: 16px; height: 16px;
    border-radius: 50%;
    background: var(--brand-blue);
    flex: none;
  }
  .brand__name { font-size: 36px; line-height: 1; letter-spacing: .5px; }
  .brand__sub { display: block; font-size: 13px; letter-spacing: 5px; margin-top: 4px; }
  .card--front .brand { right: 34px; top: 52px; }
  .card--back .brand  { right: 48px; top: 214px; }

  .holder__bar {
    position: absolute; left: 0; top: 152px;
    width: 13px; height: 25px;
    background: var(--brand-blue);
  }
  .holder__name {
    position: absolute; left: 32px; top: 153px;
    font-family: "Roboto Condensed", "Arial Narrow", sans-serif;
    font-weight: 700; font-size: 21px;
    color: var(--brand-blue);
    text-transform: uppercase;
    white-space: nowrap;
  }
  .holder__titles {
    position: absolute; left: 32px; top: 177px;
    color: var(--brand-green);
    font-size: 15px; line-height: 19px;
    font-weight: 500;
    list-style: none;
  }
  .divider {
    position: absolute; left: 31px; top: 226px;
    width: 536px; height: 2px;
    background: var(--rule);
  }
  .contact {
    position: absolute; left: 33px; top: 238px;
    list-style: none;
    color: var(--text-light);
    font-size: 14px; line-height: 19.5px;
  }
  .contact li { display: flex; align-items: center; gap: 8px; white-space: nowrap; }
  .contact svg { width: 14px; height: 14px; fill: var(--brand-blue); flex: none; }
  .address {
    position: absolute; right: 33px; top: 259px;
    text-align: right; font-style: normal;
    color: var(--text-light);
    font-size: 14px; line-height: 18.5px;
    white-space: nowrap;
  }
</style>
</head>
<body>
  <section class="card card--front" aria-label="Business card front">
    <div class="brand">
      <span class="brand__dot"></span>
      <span><span class="brand__name">Pathbloom</span><span class="brand__sub">COUNSELING</span></span>
    </div>

    <span class="holder__bar"></span>
    <h1 class="holder__name">Marcus T. Whitfield, Ph.D.</h1>
    <ul class="holder__titles">
      <li>Licensed Clinical Psychologist</li>
      <li>Integrative Health Coach</li>
    </ul>

    <div class="divider"></div>

    <ul class="contact">
      <li>
        <svg viewBox="0 0 16 16" aria-hidden="true"><path d="M3.5 1l2.5 3-1.5 1.8c.9 2 2.6 3.7 4.6 4.6L10.9 9l3 2.5-1.3 2.7C7 14 2 9 1.8 3.4z"/></svg>
        (483) 555-0142
      </li>
      <li>
        <svg viewBox="0 0 16 16" aria-hidden="true"><path d="M4 1h8v4H4zM1 6h14v6h-2v3H3v-3H1zm4 4v3h6v-3z"/></svg>
        (483) 555-0186
      </li>
      <li>
        <svg viewBox="0 0 16 16" aria-hidden="true"><path d="M1 3h14v1.2L8 9 1 4.2zM1 6l7 4.8L15 6v7H1z"/></svg>
        drmarcuswhitfield@kelvora.com
      </li>
      <li>
        <svg viewBox="0 0 16 16" aria-hidden="true"><path d="M8 1a7 7 0 100 14A7 7 0 008 1zm-1 2.2C6 4.5 5.5 5.5 6.5 6.5S9 7 8.5 8.5 6 9.5 6.5 11 7 13 7 13.5A5.6 5.6 0 017 2.5zm3.5.5c1 .5 1.5 1.5 1 2.5S10 6.5 11 8s1.5 2.5 1.8 3A5.6 5.6 0 0010.5 3.7z"/></svg>
        www.pathbloomcounseling.com
      </li>
    </ul>

    <address class="address">
      4812 Ferndale Pkwy NW<br>
      Suite 730<br>
      Elmvale, OR 97530
    </address>
  </section>

  <section class="card card--back" aria-label="Business card back">
    <div class="brand">
      <span class="brand__dot"></span>
      <span><span class="brand__name">Pathbloom</span><span class="brand__sub">COUNSELING</span></span>
    </div>
  </section>
</body>
</html>
```